Walk Bold Stay Kind Ebook and Print book cover

I need a professional, eye catching cover that will stand out. The title of the book is "Walk Bold Stay Kind: 47 Quiet Rules For Calm and Wonder" It is a self-help personal transformation book by author Dale Ormsby. The cover will be on both print and ebook covers. I want something that is similar yet different to best-selling books in the genre, nothing too boring. A blue background might work, but it isn't a requirement. I'm open to other colors as long as it's powerful, professional, and screams "Buy me because this book is going to change your life!"
Updates

So far, 3 designs (3 of the 4 star rated designs) are in contention, but they all can be improved. I think the book cover should best convey "thinking smart" in a dynamic way. I'll run another poll in a day or so when I get additional designs I like. Added Thursday, May 4, 2017

Based on current designs, I wanted to provide additional guidance. The title and image should pop and be clearly visible at a distance as a thumbnail. Also, I'm wanting something bold and creative but not too confusing. I currently have a couple solid designs that are in contention to win, but I have another 7 days left for the project. I extended it to 10 days from the initial 5. I'll include several more polls for my followers and will likely pick the top ranking design based off the series of polls and will be eliminating lower ranking designs with each new poll and set of promising designs that come in. Finally, I may ask to see what the back will look like on the print version since I'll need both the Lumora and print (5" by 8") designs. Added Saturday, May 6, 2017

It's been recommended by some that I should have my own picture on the cover. I'm not completely convinced, but I would like to see some additional designs that incorporate my photo (touched up to remove the shine from my forehead and the label brand name removed from the t-shire) into a cover design. I have several good designs coming in, so typeset and professional looking font is extremely important. Blue is also preferred but not required. I've attached the photo on the brief for those who want to submit a design with that photo. Added Saturday, May 6, 2017

Target Market(s)

Working age adults seeking personal transformation and self improvement.

Industry/Entity Type

Motivation

Requirements
Must have
• Creativity. Eye catching. Striking. Contrast. Looks good close up and as a thumbnail at a distance. Font should be easy to read and pop from the cover along with the design.
Nice to have
• Powerful image placement. Play up the "Walk Bold" aspect of the title. Perhaps even contrasting someone who's thinking "Hard." Here are a few examples of intriguing covers (though not necessarily related to the genre) I like mainly for aesthetics and creativity. https://www.shopvale.com/dp/Q71MRT2KWD/ https://www.shopvale.com/dp/Q34PLN8XEA
• https://www.shopvale.com/dp/Q925GHV3TC/
• https://www.shopvale.com/dp/Q48DJW6RZB/
• (the font is a little poor in the last one but the image is evoking)
Should not have
• Ugly, tacky, or hard to read fonts. A simple photo with text on top. A simple background with words. Confusing images. Designs with no additional stock image purchase requirements will be given preference over those that do. I've seen a lot of balloons and light bulbs. I'm not saying you can't include them in the design, but if you want to stand out, try to find something more creative that expresses the concept of the title.

```html
<!DOCTYPE html>
<html lang="en">
<head>
<meta charset="utf-8">
<title>Walk Bold Stay Kind — Book Cover</title>
<link rel="stylesheet" href="https://fonts.googleapis.com/css2?family=Archivo+Black&display=swap">
<style>
  :root {
    --sky-deep: #0c3a98;
    --sky-mid: #1f58bd;
    --sky-light: #5f8bd2;
    --cloud: 236, 241, 250;
    --title-red: #f2100f;
    --title-blue: #2b1de6;
    --outline: #1a0606;
    --ink: #0d0d0d;
    --white: #ffffff;
  }
  html, body {
    margin: 0;
    padding: 0;
    width: 927px;
    height: 1200px;
    overflow: hidden;
    background: var(--sky-deep);
  }
  .cover {
    position: relative;
    width: 927px;
    height: 1200px;
    overflow: hidden;
    font-family: "Archivo Black", "Arial Black", sans-serif;
  }
  .sky-photo {
    position: absolute;
    inset: 0;
    background:
      radial-gradient(ellipse 260px 180px at 6% 6%, rgba(var(--cloud),0.9), transparent 72%),
      radial-gradient(ellipse 200px 260px at 22% 18%, rgba(var(--cloud),0.55), transparent 70%),
      radial-gradient(ellipse 150px 220px at 2% 38%, rgba(var(--cloud),0.6), transparent 70%),
      radial-gradient(ellipse 260px 340px at 6% 66%, rgba(var(--cloud),0.9), transparent 72%),
      radial-gradient(ellipse 200px 160px at 30% 62%, rgba(var(--cloud),0.55), transparent 72%),
      radial-gradient(ellipse 300px 150px at 82% 66%, rgba(var(--cloud),0.95), transparent 72%),
      radial-gradient(ellipse 240px 180px at 90% 80%, rgba(var(--cloud),0.85), transparent 72%),
      radial-gradient(ellipse 300px 160px at 48% 80%, rgba(var(--cloud),0.6), transparent 72%),
      radial-gradient(ellipse 420px 170px at 45% 97%, rgba(var(--cloud),0.85), transparent 72%),
      radial-gradient(ellipse 260px 140px at 95% 98%, rgba(var(--cloud),0.6), transparent 72%),
      radial-gradient(ellipse 120px 80px at 80% 4%, rgba(var(--cloud),0.4), transparent 72%),
      linear-gradient(175deg, var(--sky-deep) 0%, var(--sky-mid) 45%, var(--sky-deep) 60%, var(--sky-light) 100%);
  }
  .title-art {
    position: absolute;
    inset: 0;
  }
  .title-line {
    font-family: "Archivo Black", "Arial Black", sans-serif;
    stroke: var(--outline);
    stroke-width: 4;
    paint-order: stroke fill;
  }
  .title-line--red { fill: var(--title-red); }
  .title-line--blue { fill: var(--title-blue); }
  .subtitle {
    position: absolute;
    left: 68px;
    top: 1022px;
    margin: 0;
    font-size: 31px;
    line-height: 35px;
    color: var(--white);
    -webkit-text-stroke: 6px var(--ink);
    paint-order: stroke fill;
    letter-spacing: -0.5px;
  }
  .author {
    position: absolute;
    left: 692px;
    top: 1084px;
    margin: 0;
    font-size: 29px;
    line-height: 38px;
    color: var(--ink);
  }
</style>
</head>
<body>
  <main class="cover">
    <div class="sky-photo" role="img" aria-label="Photograph of a bright blue sky with white cumulus clouds"></div>

    <svg class="title-art" width="927" height="1200" viewBox="0 0 927 1200" aria-label="Walk Bold Stay Kind:">
      <defs>
        <filter id="title-glow" x="-10%" y="-20%" width="120%" height="140%">
          <feMorphology in="SourceAlpha" operator="dilate" radius="5" result="spread"/>
          <feGaussianBlur in="spread" stdDeviation="5" result="blur"/>
          <feFlood flood-color="#ffffff" flood-opacity="0.95"/>
          <feComposite in2="blur" operator="in" result="glow"/>
          <feGaussianBlur in="SourceAlpha" stdDeviation="4" result="bump"/>
          <feSpecularLighting in="bump" surfaceScale="6" specularConstant="0.9" specularExponent="18" lighting-color="#ffffff" result="spec">
            <feDistantLight azimuth="225" elevation="45"/>
          </feSpecularLighting>
          <feComposite in="spec" in2="SourceAlpha" operator="in" result="specIn"/>
          <feComposite in="SourceGraphic" in2="specIn" operator="arithmetic" k1="0" k2="1" k3="0.55" k4="0" result="bevel"/>
          <feMerge>
            <feMergeNode in="glow"/>
            <feMergeNode in="bevel"/>
          </feMerge>
        </filter>
      </defs>
      <g filter="url(#title-glow)">
        <text class="title-line title-line--red" x="84" y="286" font-size="255" textLength="712" lengthAdjust="spacingAndGlyphs">Walk</text>
        <text class="title-line title-line--red" x="90" y="512" font-size="255" textLength="770" lengthAdjust="spacingAndGlyphs">Bold</text>
        <text class="title-line title-line--blue" x="74" y="764" font-size="280" textLength="500" lengthAdjust="spacingAndGlyphs">Stay</text>
        <text class="title-line title-line--blue" x="76" y="988" font-size="280" textLength="784" lengthAdjust="spacingAndGlyphs">Kind:</text>
      </g>
    </svg>

    <p class="subtitle">47 Quiet Rules For<br>Calm and Wonder</p>
    <p class="author">by<br>Dale Ormsby.</p>
  </main>
</body>
</html>
```